Business card for partnership

Plumbing and hvac company needing a minimal business card. We already have a logo i would like the front of the card just the logo and the back have all info.

Target Market(s)

Commercial facilities

Industry/Entity Type

Plumbing hvac

Contact Information for Business Card

We would like it double sided. Logo big and bold on the front and out info on the back. Our info on back would be name and position phone, email, and location

```html
<!DOCTYPE html>
<html lang="en">
<head>
<meta charset="utf-8">
<title>Kestrel Mechanical – Business Cards</title>
<link href="https://fonts.googleapis.com/css2?family=Lato:wght@400;700&family=Ubuntu:wght@500&display=swap" rel="stylesheet">
<style>
  :root {
    --backdrop: #0e0e0e;
    --card: #5a5a5a;
    --white: #ffffff;
    --label: #e6e6e6;
    --orange: #f28a3c;
    --orange-light: #f6953f;
    --orange-deep: #e76a37;
    --text-light: #f1f1f1;
  }
  * { margin: 0; padding: 0; box-sizing: border-box; }
  html, body { width: 1200px; height: 831px; overflow: hidden; background: var(--backdrop); }
  .sheet { position: relative; width: 1200px; height: 831px; font-family: "Lato", sans-serif; }

  .card {
    position: absolute; width: 452px; height: 258px;
    background: var(--card); border-radius: 17px; overflow: hidden;
  }
  .card--front { left: 131px; top: 111px; }
  .card--back-01 { left: 626px; top: 111px; }
  .card--back-02 { left: 131px; top: 425px; }
  .card--back-03 { left: 626px; top: 425px; }

  .card-label {
    position: absolute; width: 452px; text-align: center;
    font-weight: 700; font-size: 16px; letter-spacing: 2.2px; color: var(--label);
  }
  .card-label--front { left: 131px; top: 390px; }
  .card-label--back-01 { left: 626px; top: 390px; }
  .card-label--back-02 { left: 131px; top: 704px; }
  .card-label--back-03 { left: 626px; top: 704px; }

  .wordmark {
    position: absolute; left: 67px; top: 74px; width: 318px;
    color: var(--white); font-weight: 700; text-align: center; line-height: 1;
  }
  .wordmark__main { display: block; font-size: 76px; letter-spacing: 1px; }
  .wordmark__sub { display: block; font-size: 40px; letter-spacing: 1.5px; margin-top: 6px; }

  .brand-block {
    position: absolute; left: 12px; top: 12px; width: 124px; height: 124px;
    background: linear-gradient(180deg, var(--orange-light), var(--orange-deep));
  }

  .contact { position: absolute; right: 36px; text-align: right; }
  .contact__name {
    font-family: "Ubuntu", sans-serif; font-weight: 500; font-size: 23px;
    color: var(--orange); line-height: 1; letter-spacing: -0.2px;
  }
  .contact__role { font-size: 13px; color: var(--text-light); margin-top: 3px; line-height: 1; }
  .contact__line {
    display: flex; justify-content: flex-end; align-items: center; gap: 7px;
    color: var(--text-light); line-height: 1;
  }
  .contact__line--phone { font-weight: 700; font-size: 14px; margin-top: 14px; letter-spacing: 0.6px; }
  .contact__line--email { font-size: 11.5px; margin-top: 5px; }
  .contact__icon { width: 9px; height: 9px; flex: none; }

  .contact--top { top: 38px; }
  .contact--second { top: 139px; }
  .contact--single { top: 139px; }
</style>
</head>
<body>
<main class="sheet">

  <section class="card card--front">
    <div class="wordmark">
      <span class="wordmark__main">KESTREL</span>
      <span class="wordmark__sub">MECHANICAL</span>
    </div>
  </section>
  <p class="card-label card-label--front">FRONT CARD</p>

  <section class="card card--back-01">
    <div class="brand-block" aria-hidden="true"></div>
    <div class="contact contact--top">
      <p class="contact__name">DALE MORROW</p>
      <p class="contact__role">Owner</p>
      <p class="contact__line contact__line--phone">615-555-0142
        <svg class="contact__icon" viewBox="0 0 10 10"><path d="M2 0.8 L3.6 2.8 L2.8 3.8 Q4 6 6.2 7.2 L7.2 6.4 L9.2 8 L8 9.4 Q4.5 9 2.5 6.8 Q0.6 4.6 0.6 2 Z" fill="var(--orange)"/></svg>
      </p>
      <p class="contact__line contact__line--email">Dmorrow@kestrelmechanical.biz
        <svg class="contact__icon" viewBox="0 0 10 10"><rect x="0.5" y="2" width="9" height="6.5" fill="var(--orange)"/><path d="M0.8 2.3 L5 5.6 L9.2 2.3" fill="none" stroke="var(--card)" stroke-width="0.8"/></svg>
      </p>
    </div>
    <div class="contact contact--second">
      <p class="contact__name">CURTIS HALE</p>
      <p class="contact__role">Owner</p>
      <p class="contact__line contact__line--phone">615-555-0187
        <svg class="contact__icon" viewBox="0 0 10 10"><path d="M2 0.8 L3.6 2.8 L2.8 3.8 Q4 6 6.2 7.2 L7.2 6.4 L9.2 8 L8 9.4 Q4.5 9 2.5 6.8 Q0.6 4.6 0.6 2 Z" fill="var(--orange)"/></svg>
      </p>
      <p class="contact__line contact__line--email">Chale@kestrelmechanical.biz
        <svg class="contact__icon" viewBox="0 0 10 10"><rect x="0.5" y="2" width="9" height="6.5" fill="var(--orange)"/><path d="M0.8 2.3 L5 5.6 L9.2 2.3" fill="none" stroke="var(--card)" stroke-width="0.8"/></svg>
      </p>
    </div>
  </section>
  <p class="card-label card-label--back-01">BACK CARD 01</p>

  <section class="card card--back-02">
    <div class="brand-block" aria-hidden="true"></div>
    <div class="contact contact--single">
      <p class="contact__name">DALE MORROW</p>
      <p class="contact__role">Owner</p>
      <p class="contact__line contact__line--phone">615-555-0142
        <svg class="contact__icon" viewBox="0 0 10 10"><path d="M2 0.8 L3.6 2.8 L2.8 3.8 Q4 6 6.2 7.2 L7.2 6.4 L9.2 8 L8 9.4 Q4.5 9 2.5 6.8 Q0.6 4.6 0.6 2 Z" fill="var(--orange)"/></svg>
      </p>
      <p class="contact__line contact__line--email">Dmorrow@kestrelmechanical.biz
        <svg class="contact__icon" viewBox="0 0 10 10"><rect x="0.5" y="2" width="9" height="6.5" fill="var(--orange)"/><path d="M0.8 2.3 L5 5.6 L9.2 2.3" fill="none" stroke="var(--card)" stroke-width="0.8"/></svg>
      </p>
    </div>
  </section>
  <p class="card-label card-label--back-02">BACK CARD 02</p>

  <section class="card card--back-03">
    <div class="brand-block" aria-hidden="true"></div>
    <div class="contact contact--single">
      <p class="contact__name">CURTIS HALE</p>
      <p class="contact__role">Owner</p>
      <p class="contact__line contact__line--phone">615-555-0187
        <svg class="contact__icon" viewBox="0 0 10 10"><path d="M2 0.8 L3.6 2.8 L2.8 3.8 Q4 6 6.2 7.2 L7.2 6.4 L9.2 8 L8 9.4 Q4.5 9 2.5 6.8 Q0.6 4.6 0.6 2 Z" fill="var(--orange)"/></svg>
      </p>
      <p class="contact__line contact__line--email">Chale@kestrelmechanical.biz
        <svg class="contact__icon" viewBox="0 0 10 10"><rect x="0.5" y="2" width="9" height="6.5" fill="var(--orange)"/><path d="M0.8 2.3 L5 5.6 L9.2 2.3" fill="none" stroke="var(--card)" stroke-width="0.8"/></svg>
      </p>
    </div>
  </section>
  <p class="card-label card-label--back-03">BACK CARD 03</p>

</main>
</body>
</html>
```